Business Card and Letterhead for Juniper Anvil - (Have Logo)

Update 4: Removed company reg no from business card details as it looked a bit out of place. Updated services list.
UPDATE 3
Sorry, I got the address a little bit wrong, have updated it below. Sorry for any inconvenience caused.
UPDATE 2
Finally I have the details for the business cards and letterhead. Submissions already made do not have to be updated unless shortlisted, if all new submissions could include the details for me, Marcus, that would be very much appreciated and help with the final shortlist selection. I intend to share a shortlist of the three best entries with past and existing customers for their feedback and opinions. Thank you all again for your time.
Here are the details.
Marcus Telby
Web Developer
T: 01632 960 418
E: marcus@juniperanvil.example
www.juniperanvil.example
Professional Photography
Web Solutions & E-Commerce
Audio & HD Video Production
Marketing & Promotions
Identity and Branding
Juniper Anvil Ltd
Suite 20938, 3rd Floor
212-224 Orchard Lane
London, N7 9QX
Company Reg. No: 05829147
The order and the layout of the information are of course down to the design, but the company registration number should be smaller and less prominent. The formatting of the telephone and email address using a T: and an E: I am not sure about and again if it is Tel: or Email: or Icons is up to the design.
The Company No. on the letterhead should read (somewhere in small text along the bottom):
Juniper Anvil is a Ltd Company registered in England & Wales, Registration No. 05829147.
The second business card details are
Oliver Brackley
Photographer
T: 01632 960 418
E: oliver@juniperanvil.example
Everything else the same of course.
Thank you again for all the submissions so far.
END OF UPDATE 2
-
UPDATE 1: Please do not alter the logo nor the logo colours. (This was a previous pixel forum project and I am extremely happy with it. The icon can stand alone of course, but I have had to eliminate all entries that have made it black and white, or reversed the icon.) I would like to thank everyone that has participated so far and am very grateful for all your thought and time.
End of Update 1
-
Original Brief:
I have attached the logo vector file.
Following a superb logo from a previous Pixel Forum project I am now looking for a business card design and (although less important) a letterhead as well.
I must admit I tried to do it myself but could only come up with the usual amateur stuff that in comparison to the quality of the logo looked awful.
About Us
Juniper Anvil Ltd will be a new company due to start in January. It is really just me (a web developer) and my friend (a photographer). We will be aiming at the usual small to medium sized businesses in the local area, selling various digital services including photographic services to the public, web hosting and development, commercial photography, modelling services (not us!), full video and film production and possibly a bit of marketing as well. (Really it is anything we can do professionally all lumped together! We met running seperate businesses which have both since closed)
We will not be competing on price. We plan to be expensive but fair. Certainly not the cheapest.
What we are looking for
Business Card
I imagine a double sided business card, which will be used for more than one person. I imagine the front to be the same for everyone and the persons details to be on the back, although this is of course only my thoughts and I am of course completely open to any ideas.
The card could also have a services list or a bit about what we do on it. It might feature the website address, our business address (mail forwarding address) or our registered company number.
Or it might have none of that, we are completely open to any ideas and have no real fixed opinions. I just want it to be really nice :-)
Letterhead (secondary importance)
We will make our decision primarily on the business card, although a mathcing letterhead would be fantastic. Something standardish in format and simple, although again, all ideas are welcomed.
I hope that is enough information but if you have any questions I will answer them as fully and as quickly as possible.
Thank you once again and I really look forward to seeing your ideas and picking a winner.
Marcus T.
Small businesses AND the general public
Film Production

```html
<!DOCTYPE html>
<html lang="en">
<head>
<meta charset="utf-8">
<title>Juniper Anvil – Stationery</title>
<link rel="stylesheet" href="https://fonts.googleapis.com/css2?family=Open+Sans:wght@400;600;700&family=Russo+One&display=swap">
<style>
  :root {
    --stage: #000000;
    --paper: #ffffff;
    --ink: #3a3a3a;
    --ink-soft: #555555;
    --brand-red: #c0161c;
    --band-red: #b81d1d;
    --band-red-light: #d2553a;
    --rule-dark: #4a4a4a;
    --rule-light: #d8d8d8;
    --label: #ffffff;
  }
  * { box-sizing: border-box; margin: 0; padding: 0; }
  html, body { width: 1200px; height: 900px; overflow: hidden; background: var(--stage); }
  body { position: relative; font-family: "Open Sans", Arial, sans-serif; color: var(--ink); }

  .sheet, .card { position: absolute; background: var(--paper); overflow: hidden; }

  /* Brand name lockup */
  .brand { position: absolute; display: flex; align-items: center; gap: 7px; }
  .brand__mark { width: 16px; height: 16px; background: var(--brand-red); }
  .brand__name { font-weight: 700; color: var(--ink); text-transform: uppercase; letter-spacing: 0.5px; white-space: nowrap; }

  /* Red band and grey rule */
  .band { position: absolute; left: 0; right: 0;
    background: linear-gradient(90deg, var(--band-red) 0%, var(--band-red) 55%, var(--band-red-light) 75%, var(--band-red) 100%); }
  .rule { position: absolute; left: 0; right: 0;
    background: linear-gradient(90deg, var(--rule-dark) 0%, var(--rule-light) 60%, var(--rule-dark) 100%); }

  .services { position: absolute; list-style: none; color: var(--ink-soft); white-space: nowrap; }

  /* Letterhead */
  .letterhead { left: 17px; top: 27px; width: 601px; height: 850px; }
  .letterhead .brand { left: 394px; top: 38px; }
  .letterhead .brand__mark { width: 20px; height: 20px; }
  .letterhead .brand__name { font-size: 19px; }
  .letterhead .services { left: 434px; top: 82px; font-size: 9px; line-height: 15px; }
  .letterhead__footer { position: absolute; left: 0; right: 0; top: 752px; text-align: center; font-size: 8.5px; line-height: 14px; color: var(--ink-soft); }
  .letterhead__footer strong { color: var(--ink); font-weight: 700; }
  .letterhead__footer .sep { color: var(--brand-red); padding: 0 4px; }
  .letterhead__legal { font-size: 5.5px; line-height: 10px; }
  .letterhead .rule { top: 792px; height: 6px; }
  .letterhead .band { top: 798px; bottom: 0; }

  /* Cards */
  .card .brand__name { font-size: 16px; }

  .card--front { left: 774px; top: 71px; width: 309px; height: 199px; }
  .card--front .band { top: 0; height: 127px; }
  .card--front .rule { top: 127px; height: 8px; }
  .card--front .brand { right: 18px; top: 155px; }

  .card--back { width: 309px; height: 199px; }
  .card--developer { left: 774px; top: 333px; }
  .card--photographer { left: 773px; top: 597px; }
  .card--back .brand { right: 18px; top: 22px; }
  .card--back .rule { top: 160px; height: 8px; }
  .card--back .band { top: 168px; bottom: 0; }

  .person { position: absolute; left: 18px; top: 39px; font-size: 8.5px; line-height: 13px; color: var(--ink-soft); white-space: nowrap; }
  .person__name { font-weight: 700; color: var(--brand-red); font-size: 10px; line-height: 15px; text-transform: uppercase; letter-spacing: 0.3px; }
  .person__role { font-weight: 700; color: var(--ink); font-size: 9px; line-height: 14px; margin-bottom: 11px; }
  .person b, .person__web { font-weight: 700; color: var(--ink); }
  .card--back .services { left: 180px; top: 56px; font-size: 7.3px; line-height: 13px; }
  .company { position: absolute; left: 18px; top: 125px; font-size: 8.3px; line-height: 13px; color: var(--ink-soft); white-space: nowrap; }
  .company strong { color: var(--ink); font-weight: 700; }
  .company__reg { font-size: 5.5px; line-height: 8px; }

  .label { position: absolute; width: 320px; text-align: center; color: var(--label);
    font-family: "Russo One", Arial, sans-serif; font-size: 23px; letter-spacing: 1px; }
  .label--front { left: 770px; top: 277px; }
  .label--developer { left: 770px; top: 536px; }
  .label--photographer { left: 770px; top: 812px; }
</style>
</head>
<body>

<section class="sheet letterhead">
  <div class="brand"><span class="brand__mark"></span><span class="brand__name">Juniper Anvil</span></div>
  <ul class="services">
    <li>Professional Photography</li>
    <li>Web Solutions &amp; E-Commerce</li>
    <li>Audio &amp; HD Video Production</li>
    <li>Marketing &amp; Promotions</li>
    <li>Design, Creation and Inspiration</li>
  </ul>
  <footer class="letterhead__footer">
    <p><strong>Juniper Anvil Ltd</strong> Suite 20938, 3rd Floor, 212-224 Orchard Lane, London, N7 9QX</p>
    <p><b>T:</b> 01632 960 418 <span class="sep">|</span> <strong>www.juniperanvil.example</strong></p>
    <p class="letterhead__legal">Juniper Anvil is a Ltd Company registered in England &amp; Wales, Registration No. 05829147.</p>
  </footer>
  <div class="rule"></div>
  <div class="band" role="img" aria-label="Red band with a repeating small brand-icon pattern"></div>
</section>

<section class="card card--front">
  <div class="band" role="img" aria-label="Red band with a repeating small brand-icon pattern"></div>
  <div class="rule"></div>
  <div class="brand"><span class="brand__mark"></span><span class="brand__name">Juniper Anvil</span></div>
</section>
<p class="label label--front">Card Front</p>

<section class="card card--back card--developer">
  <div class="brand"><span class="brand__mark"></span><span class="brand__name">Juniper Anvil</span></div>
  <div class="person">
    <p class="person__name">Marcus Telby</p>
    <p class="person__role">Web Developer</p>
    <p><b>T:</b> 01632 960 418</p>
    <p><b>E:</b> marcus@juniperanvil.example</p>
    <p class="person__web">www.juniperanvil.example</p>
  </div>
  <ul class="services">
    <li>Professional Photography</li>
    <li>Web Solutions &amp; E-Commerce</li>
    <li>Audio &amp; HD Video Production</li>
    <li>Marketing &amp; Promotions</li>
    <li>Design, Creation and Inspiration</li>
  </ul>
  <div class="company">
    <p><strong>Juniper Anvil Ltd</strong></p>
    <p>Suite 20938, 3rd Floor, 212-224 Orchard Lane, London, N7 9QX</p>
    <p class="company__reg">Company Reg. No: 05829147</p>
  </div>
  <div class="rule"></div>
  <div class="band" role="img" aria-label="Red band with a repeating small brand-icon pattern"></div>
</section>
<p class="label label--developer">Card Back - Marcus</p>

<section class="card card--back card--photographer">
  <div class="brand"><span class="brand__mark"></span><span class="brand__name">Juniper Anvil</span></div>
  <div class="person">
    <p class="person__name">Oliver Brackley</p>
    <p class="person__role">Photographer</p>
    <p><b>T:</b> 01632 960 418</p>
    <p><b>E:</b> oliver@juniperanvil.example</p>
    <p class="person__web">www.juniperanvil.example</p>
  </div>
  <ul class="services">
    <li>Professional Photography</li>
    <li>Web Solutions &amp; E-Commerce</li>
    <li>Audio &amp; HD Video Production</li>
    <li>Marketing &amp; Promotions</li>
    <li>Design, Creation and Inspiration</li>
  </ul>
  <div class="company">
    <p><strong>Juniper Anvil Ltd</strong></p>
    <p>Suite 20938, 3rd Floor, 212-224 Orchard Lane, London, N7 9QX</p>
    <p class="company__reg">Company Reg. No: 05829147</p>
  </div>
  <div class="rule"></div>
  <div class="band" role="img" aria-label="Red band with a repeating small brand-icon pattern"></div>
</section>
<p class="label label--photographer">Card Back - Oliver</p>

</body>
</html>
```